Plumvex Healthy Juices paper cups

We need a packaging design on paper cups of fruit shakes /juices we are selling. We want to communicate sexy body, health and refreshing. We wanted to stick to white and red color only but we are open to all suggestions...however, we wanted red to be dominating color.

I attached a sample but I believe that there is something more than this glass. I hope to see better, much better than this. Though we can use this cup but some finishing touch or better design with the red stripes will be ok.
Updates

I now included the previous packaging design but we want to communicate sexy, health and refreshing drink. I also downloaded our cart / kiosk for your guide. Thank you.

Hi to all designers, good day. I added jiva brisk to become your inspirations in designing our plumvex cups. Many thanks!

Reason: To attract more designs and give time to designers to conceptualise.

Hi Designers, i would like to apologise sincerely but the business is no longer viable due to management decision. For that reason, I am no longer continuing this venture. Thank you for your understanding.

Target Market(s)

male and female who are health conscious

Industry/Entity Type

Health

Colors
eb1f27
ffffff

Requirements
Must have
• red and white color primary colors

```html
<!DOCTYPE html>
<html lang="en">
<head>
<meta charset="utf-8">
<title>Plumvex Healthy Juices – cup wrap</title>
<link rel="stylesheet" href="https://fonts.googleapis.com/css2?family=Open+Sans:wght@400;700&display=swap">
<style>
  :root {
    --red: #c41423;
    --white: #ffffff;
    --blue: #229bd8;
    --green: #b3d66e;
    --ink: #1d1d1b;
    --shelf: #ebe7e3;
  }
  html, body {
    margin: 0;
    padding: 0;
    overflow: hidden;
    background: var(--white);
    font-family: "Open Sans", sans-serif;
  }
  .sheet {
    position: relative;
    width: 1200px;
    height: 1200px;
    overflow: hidden;
    background: var(--white);
  }
  .wrap { position: absolute; display: block; }
  .wrap--main   { left: 125px; top: 90px;  width: 420px; height: 652px; }
  .shelf-panel  { position: absolute; left: 678px; top: 127px; width: 397px; height: 611px; background: var(--shelf); }
  .wrap--shelf  { left: 750px; top: 330px; width: 251px; height: 390px; }
  .variant-bg   { position: absolute; top: 806px; height: 372px; width: 244px; }
  .variant-bg--green { left: 634px; background: var(--green); }
  .variant-bg--blue  { left: 945px; background: var(--blue); }
  .wrap--small  { top: 812px; width: 237px; height: 368px; }
  .wrap--blue-stripes  { left: 18px; }
  .wrap--green-stripes { left: 326px; }
  .wrap--on-green      { left: 638px; }
  .wrap--on-blue       { left: 949px; }

  .fruit-art { fill: var(--fruit-fill); stroke: var(--ink); stroke-width: 3; }

  .theme-red      { --stripe: var(--red);   --ring: var(--white); --rim: var(--red);   --fruit-fill: url(#fruit-red); }
  .theme-blue     { --stripe: var(--blue);  --ring: var(--white); --rim: var(--red);   --fruit-fill: url(#fruit-blue); }
  .theme-green    { --stripe: var(--green); --ring: var(--white); --rim: var(--red);   --fruit-fill: url(#fruit-green); }
  .theme-on-green { --stripe: var(--red);   --ring: var(--white); --rim: var(--white); --fruit-fill: url(#fruit-on-green); }
  .theme-on-blue  { --stripe: var(--red);   --ring: var(--white); --rim: var(--white); --fruit-fill: url(#fruit-on-blue); }
</style>
</head>
<body>
<main class="sheet">
  <svg width="0" height="0" style="position:absolute" aria-hidden="true">
    <defs>
      <linearGradient id="fruit-red" x1="0" y1="0" x2="0" y2="1">
        <stop offset="0" stop-color="#c41423"/><stop offset="0.45" stop-color="#ffffff"/><stop offset="1" stop-color="#ffffff"/>
      </linearGradient>
      <linearGradient id="fruit-blue" x1="0" y1="0" x2="0" y2="1">
        <stop offset="0" stop-color="#229bd8"/><stop offset="0.45" stop-color="#ffffff"/><stop offset="1" stop-color="#ffffff"/>
      </linearGradient>
      <linearGradient id="fruit-green" x1="0" y1="0" x2="0" y2="1">
        <stop offset="0" stop-color="#b3d66e"/><stop offset="0.45" stop-color="#ffffff"/><stop offset="1" stop-color="#ffffff"/>
      </linearGradient>
      <linearGradient id="fruit-on-green" x1="0" y1="0" x2="0" y2="1">
        <stop offset="0" stop-color="#c41423"/><stop offset="0.45" stop-color="#b3d66e"/><stop offset="1" stop-color="#b3d66e"/>
      </linearGradient>
      <linearGradient id="fruit-on-blue" x1="0" y1="0" x2="0" y2="1">
        <stop offset="0" stop-color="#c41423"/><stop offset="0.45" stop-color="#229bd8"/><stop offset="1" stop-color="#229bd8"/>
      </linearGradient>

      <symbol id="cup-wrap" viewBox="0 0 420 652">
        <g class="stripes" fill="var(--stripe)">
          <rect x="10"  y="200" width="72" height="452"/>
          <rect x="118" y="130" width="72" height="522"/>
          <rect x="225" y="125" width="72" height="527"/>
          <rect x="333" y="240" width="72" height="412"/>
        </g>
        <g class="fruit-row">
          <rect class="fruit-art" x="6"   y="14" width="78" height="194" rx="34" role="img" aria-label="Pear illustration with juice splash"/>
          <rect class="fruit-art" x="100" y="8"  width="96" height="168" rx="38" role="img" aria-label="Strawberry illustration with juice splash"/>
          <rect class="fruit-art" x="220" y="8"  width="86" height="148" rx="36" role="img" aria-label="Apple illustration with juice splash"/>
          <rect class="fruit-art" x="328" y="92" width="82" height="160" rx="32" role="img" aria-label="Cherries illustration with juice splash"/>
        </g>
        <g class="label-badge">
          <ellipse cx="209" cy="400" rx="145" ry="95" fill="var(--ring)" stroke="var(--rim)" stroke-width="2"/>
          <ellipse cx="209" cy="400" rx="133" ry="83" fill="var(--red)"/>
        </g>
      </symbol>
    </defs>
  </svg>

  <svg class="wrap wrap--main theme-red" viewBox="0 0 420 652" aria-label="Plumvex Healthy Juices cup wrap, red"><use href="#cup-wrap"/></svg>

  <div class="shelf-panel"></div>
  <svg class="wrap wrap--shelf theme-red" viewBox="0 0 420 652" aria-label="Plumvex Healthy Juices cup wrap, red"><use href="#cup-wrap"/></svg>

  <svg class="wrap wrap--small wrap--blue-stripes theme-blue" viewBox="0 0 420 652" aria-label="Cup wrap, blue stripes"><use href="#cup-wrap"/></svg>
  <svg class="wrap wrap--small wrap--green-stripes theme-green" viewBox="0 0 420 652" aria-label="Cup wrap, green stripes"><use href="#cup-wrap"/></svg>

  <div class="variant-bg variant-bg--green"></div>
  <svg class="wrap wrap--small wrap--on-green theme-on-green" viewBox="0 0 420 652" aria-label="Cup wrap, red on green"><use href="#cup-wrap"/></svg>

  <div class="variant-bg variant-bg--blue"></div>
  <svg class="wrap wrap--small wrap--on-blue theme-on-blue" viewBox="0 0 420 652" aria-label="Cup wrap, red on blue"><use href="#cup-wrap"/></svg>
</main>
</body>
</html>
```